Wordpress Web Design For Midlife Lane.com

We're looking to update the design for www.midlifelane.example. The website provides news and views for people aged 50 plus.

We want to use Wordpress as the content management tool and incorporate postwren to manage subscribers to our monthly newsletter.

In terms of design, we're looking for something simple and straightforward, we quite like the elder hub site, so something like that would be good. http://www.elderhub.example.org
Updates

Project Deadline Extended
Reason: Dear All, Due to the Xmas break in the UK I've decided to extend the deadline by 7 days. Thanks for all your submissions, we will be making a decision shortly. Please note, as per the original brief, we are only interested in fully coded sites uploaded to our hosting provider. Please withdraw your design if you are not able to offer this complete solution. Thanks and good wishes to all!

Requirements
Must have
• Fully working wordpress templates that allow us to easily manage the website content. Easy for readers to use, navigate and read the content.
• Ideally a'turnkey' solution - the website built and ready for us to use wordpress to populate with content.

```html
<!DOCTYPE html>
<html lang="en">
<head>
<meta charset="utf-8">
<title>Register – Midlife Lane.com</title>
<link href="https://fonts.googleapis.com/css2?family=Open+Sans:wght@400;600;700&family=Ubuntu:wght@400;500&display=swap" rel="stylesheet">
<style>
:root{
  --green:#7fa81a;
  --green-dark:#5e8a0b;
  --green-light:#9cc22a;
  --footer:#6a9a0e;
  --footer-bar:#93bd22;
  --navy:#1c3f8f;
  --ink:#444;
  --muted:#777;
  --line:#ddd;
  --page:#efefef;
  --white:#fff;
  --plum:#8b1a5e;
}
*{box-sizing:border-box;margin:0;padding:0}
html,body{width:960px;height:1200px;overflow:hidden}
body{position:relative;background:var(--page);font-family:"Open Sans",Arial,sans-serif;color:var(--ink)}
.abs{position:absolute}
.header{left:0;top:0;width:960px;height:76px;background:var(--white)}
.brand{left:84px;top:16px;display:flex;align-items:center;gap:8px;font-size:20px;font-weight:700;color:var(--green-dark)}
.brand-dot{width:44px;height:44px;border-radius:50%;background:var(--green-light)}
.toplinks{left:624px;top:12px;font-size:9px;color:var(--muted)}
.toplinks span{margin-right:32px}
.socials{left:756px;top:11px;display:flex;gap:3px}
.socials i{display:block;width:13px;height:13px;background:#8aa;border-radius:2px}
.call{left:588px;top:46px;font-size:10px;color:var(--ink)}
.call b{font-weight:400;color:var(--navy)}
.search{left:713px;top:40px;width:123px;height:24px;border:1px solid var(--line);background:#f6f6f6;font-size:9px;color:#999;padding:6px 6px}
.search-btn{left:836px;top:40px;width:51px;height:24px;background:var(--green-light);color:#fff;font-size:9px;font-weight:700;text-align:center;line-height:24px;border-radius:0 2px 2px 0}
.nav-top{left:0;top:77px;width:960px;height:5px;background:#333}
.nav{left:0;top:82px;width:960px;height:42px;background:linear-gradient(var(--green-light),var(--green));display:flex;align-items:center;padding-left:101px}
.nav a{color:#fff;font-family:Arial,sans-serif;font-size:11px;text-decoration:none;margin-right:33px}
.card{background:var(--white);border:1px solid #e3e3e3}
.newsletter{left:76px;top:140px;width:190px;height:182px;background:linear-gradient(var(--green-dark),var(--green));border-top:5px solid #333;color:#fff;padding:14px 14px}
.newsletter h3{font-weight:400;font-size:13px;letter-spacing:.5px}
.newsletter h3 b{display:block;font-weight:600;font-size:14px;letter-spacing:1px}
.newsletter p{font-size:9.5px;letter-spacing:.8px;line-height:12px;margin-top:14px;width:120px}
.envelope{left:104px;top:88px}
.nl-input{left:12px;top:142px;width:148px;height:21px;background:#fff;color:#888;font-size:8px;padding:5px 10px}
.nl-go{left:160px;top:142px;width:20px;height:21px;background:#444}
.login{left:76px;top:339px;width:190px;height:144px;padding:6px 26px}
.login h4{font-weight:400;font-size:12px;color:var(--green-dark)}
.field{height:24px;background:#f3f3f3;border:1px solid #e3e3e3;font-size:9px;color:#888;padding:5px 10px;margin-top:5px}
.login-btn{left:23px;top:89px;width:146px;height:36px;background:linear-gradient(var(--green-light),var(--green));border:1px solid var(--green-dark);color:var(--ink);font-weight:700;font-size:11px;text-align:center;line-height:36px;border-radius:2px}
.forgot{left:0;top:128px;width:190px;text-align:center;font-size:8px;color:#aaa;letter-spacing:.5px}
.vote{left:76px;top:500px;width:190px;height:172px;background:linear-gradient(135deg,#b7a9a0,#8e7a78 60%,#6d5460)}
.vote-tag{left:0;top:124px;background:var(--plum);color:#fff;padding:2px 5px;font-size:13px;line-height:16px}
.vote-tag b{font-size:15px}
.vote-badge{left:128px;top:110px;width:58px;height:58px;border-radius:50%;background:var(--plum);border:2px solid #fff}
.partners{left:76px;top:683px;width:190px;height:215px}
.partner-name{width:190px;text-align:center;font-size:18px;font-weight:700;color:var(--navy);left:0}
.partner-dot{display:inline-block;width:12px;height:12px;border-radius:50%;background:var(--plum);margin-right:6px;vertical-align:middle}
.quote{left:42px;top:81px;width:100px;height:49px;background:linear-gradient(#fff,#e6e6ee);border:1px solid #ccd;text-align:center;font-size:9px;color:var(--plum);padding-top:3px}
.quote span{display:block;margin:4px auto 0;width:72px;height:18px;background:#3a6fc4;color:#fff;font-size:11px;font-weight:700;border-radius:4px;line-height:18px}
.main{left:284px;top:139px;width:395px;height:646px}
.main h1{position:absolute;left:18px;top:14px;font-weight:400;font-size:20px;color:var(--navy);font-family:Arial,sans-serif}
.intro{position:absolute;left:12px;top:52px;width:370px;font-size:10.5px;line-height:19.5px;color:#666;padding-bottom:9px;border-bottom:1px solid #e6e6e6}
.sec{left:18px;font-size:11px;font-weight:700;color:#333}
.row{left:0;width:395px;height:24px}
.row label{position:absolute;right:254px;top:5px;font-size:11px;color:#444;white-space:nowrap}
.row label i{font-style:normal;color:#c33}
.row .inp{position:absolute;left:149px;top:0;width:180px;height:24px;border:1px solid #ccc;border-radius:2px;font-family:Arial,sans-serif;font-size:11px;color:#aaa;padding:5px 6px}
.submit{left:149px;width:48px;height:19px;background:#eee;border:1px solid #ccc;font-size:9px;color:#666;text-align:center;line-height:17px;border-radius:2px}
.banner{left:284px;top:798px;width:394px;height:50px;background:#fff;border:1px solid #e3e3e3}
.banner-photo{left:0;top:0;width:90px;height:48px;background:linear-gradient(90deg,#a5987e,#d8ccb4)}
.banner-text{left:122px;top:10px;font-family:Arial,sans-serif;line-height:17px}
.banner-text b{display:block;color:var(--plum);font-size:16px;font-weight:400}
.banner-text span{color:#3a9bd6;font-size:16px}
.banner-mark{left:340px;top:17px;font-size:9px;color:#333}
.donate{left:696px;top:139px;width:189px;height:215px;border-top:4px solid #333;background:var(--green-light)}
.donate-photo{left:0;top:0;width:189px;height:89px;background:linear-gradient(135deg,#d9c5b1,#b8d0e0)}
.donate h3{left:9px;top:108px;color:#fff;font-size:15px;font-weight:700;letter-spacing:.5px}
.donate p{left:9px;top:140px;width:170px;color:#fff;font-size:9.5px;line-height:13.5px;letter-spacing:.3px}
.donate a{left:103px;top:191px;color:#e8f3c4;font-size:9px;letter-spacing:.8px}
.insurer{left:696px;top:364px;width:189px;height:173px;display:flex;flex-direction:column;align-items:center;justify-content:center}
.insurer .sq{width:36px;height:36px;background:#2aa3d8;margin-bottom:10px}
.insurer b{font-size:28px;font-weight:400;color:#333;line-height:30px}
.insurer span{font-size:15px;color:#333}
.social{left:696px;top:547px;width:189px;height:228px}
.social-inner{left:12px;top:9px;width:164px;height:203px;border:1px solid #bbb}
.social-head{left:8px;top:8px;display:flex;gap:8px}
.social-head .dot{width:44px;height:44px;border-radius:50%;background:var(--green-light)}
.social-head b{font-size:11px;font-weight:400;color:#111}
.like{display:block;margin-top:4px;width:40px;height:14px;background:#4a66a0;color:#fff;font-size:9px;text-align:center;line-height:14px}
.count{left:8px;top:64px;font-size:8.5px;color:#333;border-top:1px solid #ddd;padding-top:6px;width:146px}
.count b{color:var(--navy)}
.faces{left:8px;top:84px;display:grid;grid-template-columns:repeat(3,42px);gap:3px}
.faces i{display:block;width:42px;height:42px;background:#777}
.faces i:nth-child(2n){background:#555}
.faces i:nth-child(3){background:#99a}
.faces i:nth-child(5){background:#3a8}
.plugin{left:8px;top:182px;width:146px;border-top:1px solid #ddd;padding-top:4px;font-size:7.5px;color:#4a66a0}
.footer{left:0;top:924px;width:960px;height:238px;background:var(--footer);border-top:4px solid #333;font-family:Ubuntu,Arial,sans-serif;color:#fff}
.fcol{top:30px}
.fcol h5{font-size:9.5px;font-weight:500;margin-bottom:26px}
.about{left:94px;width:180px;font-size:10px;line-height:16px}
.menu{left:304px;font-size:10.5px;font-weight:500;line-height:20px;top:30px}
.menu h5{margin-bottom:12px}
.post-photo{left:514px;top:51px;width:179px;height:88px;background:linear-gradient(135deg,#d3bea9,#9aa8b8)}
.post-title{left:515px;top:151px;width:180px;font-size:10.5px;font-weight:500;line-height:16px}
.post-date{left:515px;top:187px;font-size:8.5px;color:#a4c65e}
.comment{left:725px;width:180px;display:flex;gap:9px;font-size:9.5px;line-height:16px}
.comment i{flex:none;width:34px;height:32px;background:#8c7d6e;margin-top:2px}
.sep{left:725px;top:110px;width:180px;border-top:1px dotted #cfe39a}
.footbar{left:0;top:1162px;width:960px;height:38px;background:var(--footer-bar);font-family:Ubuntu,Arial,sans-serif;color:#fff;font-size:10px;padding:11px 94px;display:flex;justify-content:space-between}
</style>
</head>
<body>

<header class="abs header">
  <div class="abs brand"><span class="brand-dot"></span>Midlife Lane.com</div>
  <div class="abs toplinks"><span>About Us</span><span>Contact</span></div>
  <div class="abs socials"><i></i><i></i><i></i><i></i><i></i><i></i><i></i></div>
  <div class="abs call">Call us now <b>800-555-0142</b></div>
  <div class="abs search">Search</div>
  <div class="abs search-btn">Search</div>
</header>
<div class="abs nav-top"></div>
<nav class="abs nav">
  <a>HOME</a><a>TRAVEL</a><a>HEALTH</a><a>HOBBIES</a><a>LIFESTYLE</a><a>INSURANCE</a><a>LEGAL</a><a>COMPETITIONS</a><a>SURVEY</a>
</nav>

<aside class="abs newsletter">
  <h3>Subscribe to the <b>Weekly Newsletters</b></h3>
  <p>Keep up to date Sign up for our fortnightly newsletter</p>
  <svg class="abs envelope" width="64" height="54" viewBox="0 0 64 54" aria-hidden="true">
    <path d="M4 10 L54 4 L58 40 L8 46 Z" fill="#9be040"/>
    <path d="M4 10 L32 30 L54 4" fill="none" stroke="#dff7b0" stroke-width="2"/>
    <path d="M24 44 L30 52 L34 43" fill="#9be040"/>
  </svg>
  <div class="abs nl-input">email address</div>
  <div class="abs nl-go"><svg width="20" height="21" viewBox="0 0 20 21"><path d="M8 7 L12 10.5 L8 14" fill="none" stroke="#fff" stroke-width="1.5"/></svg></div>
</aside>

<aside class="abs card login">
  <h4>Member Login</h4>
  <div class="field">username</div>
  <div class="field">password</div>
  <div class="abs login-btn">Login</div>
  <div class="abs forgot">forgot password?</div>
</aside>

<div class="abs vote" role="img" aria-label="Photo of smiling older women at a party">
  <div class="abs vote-tag">Raise a smile<br><b>#VoteElderHub</b></div>
  <div class="abs vote-badge"></div>
</div>

<aside class="abs card partners">
  <div class="abs partner-name" style="top:27px"><span class="partner-dot"></span>elder hub</div>
  <div class="abs quote">get a quote today<span>click here</span></div>
  <div class="abs partner-name" style="top:150px"><span class="partner-dot"></span>elder hub</div>
</aside>

<main class="abs card main">
  <h1>Register</h1>
  <p class="intro">This is some dummy copy. You’re not really supposed to read this dummy copy, it is just a place holder for people who need some type to visualize what the actual copy might look like if it were real content.</p>
  <div class="abs sec" style="top:138px">Personal Info</div>
  <div class="abs row" style="top:166px"><label>First Name <i>*</i></label><div class="inp">Ex: John</div></div>
  <div class="abs row" style="top:206px"><label>Last Name <i>*</i></label><div class="inp">Ex: Doe</div></div>
  <div class="abs row" style="top:247px"><label>Nice Name</label><div class="inp">Ex: John Doe</div></div>
  <div class="abs row" style="top:288px"><label>Display Name</label><div class="inp">Ex: John Doe</div></div>
  <div class="abs row" style="top:328px"><label>Website</label><div class="inp">Ex: http://www.website.com</div></div>
  <div class="abs sec" style="top:370px">Account Info</div>
  <div class="abs row" style="top:397px"><label>Username <i>*</i></label><div class="inp">Ex: johndoe</div></div>
  <div class="abs row" style="top:438px"><label>E-mail <i>*</i></label><div class="inp">Ex: johndoe@email.com</div></div>
  <div class="abs row" style="top:479px"><label>Password <i>*</i></label><div class="inp">Password</div></div>
  <div class="abs row" style="top:520px"><label>Repeat Password <i>*</i></label><div class="inp">Repeat Password</div></div>
  <div class="abs submit" style="top:561px">Submit</div>
</main>

<div class="abs banner">
  <div class="abs banner-photo" role="img" aria-label="Photo of a smiling older couple"></div>
  <div class="abs banner-text"><b>over 50s life cover</b><span>that ticks more boxes</span></div>
  <div class="abs banner-mark">Kinfold</div>
</div>

<aside class="abs donate">
  <div class="abs donate-photo" role="img" aria-label="Photo of a grandfather with his family"></div>
  <h3 class="abs">Donate</h3>
  <p class="abs">Help us reach the thousands of older people who feel isolated and alone.</p>
  <a class="abs">Donate Now &gt;&gt;</a>
</aside>

<aside class="abs card insurer">
  <div class="sq"></div>
  <b>Kinfold</b>
  <span>Mutual Assurance</span>
</aside>

<aside class="abs card social">
  <div class="abs social-inner">
    <div class="abs social-head"><span class="dot"></span><div><b>Midlife Lane</b><span class="like">Like</span></div></div>
    <div class="abs count">7,216 people like <b>Midlife Lane</b></div>
    <div class="abs faces" role="img" aria-label="Grid of follower profile photos"><i></i><i></i><i></i><i></i><i></i><i></i></div>
    <div class="abs plugin">Social plugin</div>
  </div>
</aside>

<footer class="abs footer">
  <div class="abs fcol about"><h5>ABOUT MIDLIFE LANE</h5>We believe that age needs respect. It needs kindness. Sometimes it needs help. Because there is strength in numbers, Senior Link and Care Aid have joined forces to become Elder Hub – so that we can be here for everyone in later life.<br>01632 960418 or 01632 960772<br><br><b style="font-weight:500">email: ann@midlifelane.example</b></div>
  <div class="abs fcol menu"><h5>MAIN MENU</h5>TRAVEL<br>HEALTH<br>HOBBIES<br>LIFESTYLE<br>INSSURANCE<br>SURVEY</div>
  <div class="abs fcol" style="left:515px"><h5>RECENT POSTS</h5></div>
  <div class="abs post-photo" role="img" aria-label="Photo of older friends giving a thumbs up"></div>
  <div class="abs post-title">Example of a Post with Comments thanks</div>
  <div class="abs post-date">16th Dec 2013</div>
  <div class="abs fcol" style="left:725px"><h5>RECENT COMMENTS</h5></div>
  <div class="abs comment" style="top:51px"><i role="img" aria-label="Commenter avatar"></i><span>Marta Velin: This is some dummy copy. You're not really suppo…</span></div>
  <div class="abs sep"></div>
  <div class="abs comment" style="top:118px"><i role="img" aria-label="Commenter avatar"></i><span>Marta Velin: In today's competitive market environment, the b…</span></div>
</footer>
<div class="abs footbar"><span>Copyright © 2013 Midlife Lane Inc. All Rights Reserved</span><span>Designed by : Brightfold Studio</span></div>

</body>
</html>
```